Website Design for Brand New Wedding Sustainability Initiative

Our brand new wedding initiative works to make weddings more sustainable and help to change lives in the developing world, all while ensuring that the wedding guests have an enhanced "feel good" factor and a wedding experience like never before!

We have attached our website brief, as well as our logo, and a very short video for you to watch for some background information.

Please feel free to ask any additional questions - it's encouraged 😊

We would like this site to be completed in Wordpress, and built in a way which allows us to make future edits. Preferably using drag and drop builders.

Target Market(s)

Our target audience is couples who are in the process of planning their wedding day.
These people are in the process of deciding upon how they can make their special day stand out and be a day to remember.

They are under a lot of pressure due to the stresses of planning their special day and have a lot of factors to consider.

Industry/Entity Type

Wedding

Coding

Coded - Design and coding required

Font styles to use
Sans Serif

Requirements
Must have
• We would like this site to be completed in Wordpress, and built in a way which allows us to make future edits. Preferably using drag and drop builders.

```html
<!DOCTYPE html>
<html lang="en">
<head>
<meta charset="utf-8">
<title>Evergreen Vows Weddings</title>
<link rel="stylesheet" href="https://fonts.googleapis.com/css2?family=Bodoni+Moda:wght@400;600;700&family=Poppins:wght@300;400;500;600&display=swap">
<style>
:root{
  --green:#0c6e00;
  --green-bright:#33cc0a;
  --ink:#333;
  --muted:#777;
  --field:#f4f4f4;
  --section-grey:#f6f6f6;
  --white:#fff;
}
*{box-sizing:border-box;margin:0;padding:0}
html,body{width:1200px;height:2640px;overflow:hidden}
body{position:relative;background:var(--white);font-family:"Poppins",sans-serif;color:var(--ink)}
.backdrop-top{position:absolute;left:0;top:0;width:1200px;height:565px;background:var(--green)}
.page{position:absolute;left:147px;top:129px;width:907px;height:2364px;background:var(--white);box-shadow:0 10px 40px rgba(0,0,0,.35);overflow:hidden}
.abs{position:absolute}
.serif{font-family:"Bodoni Moda",serif}

.topbar{left:0;top:0;width:907px;height:30px;background:var(--green);color:var(--white);font-size:10px}
.topbar .phone{left:110px;top:8px;display:flex;align-items:center;gap:10px}
.topbar .social{right:107px;top:10px;display:flex;gap:8px}
.topbar .social span{width:9px;height:9px;border-radius:50%;background:var(--white)}

.nav{left:0;top:30px;width:907px;height:53px;background:var(--white)}
.brand{left:110px;top:14px;display:flex;align-items:center;gap:6px;color:var(--green);font-size:11px;font-weight:500;line-height:1.1}
.brand .dot{width:14px;height:14px;border-radius:50%;background:var(--green-bright)}
.menu{right:107px;top:22px;display:flex;gap:24px;font-size:9px;letter-spacing:.3px;color:#888}
.menu .active{color:var(--green);font-weight:500}

.hero{left:0;top:83px;width:907px;height:353px;background:linear-gradient(180deg,#8a7868 0%,#5b4a3c 45%,#4d5a2e 80%,#3b4a22 100%)}
.hero h1{position:absolute;left:0;width:907px;top:58px;text-align:center;color:var(--white);font-size:45px;font-weight:700;line-height:52px}
.hero .more{position:absolute;left:409px;top:239px;width:88px;height:27px;border:1px solid var(--white);color:var(--white);font-size:11px;text-align:center;line-height:25px}

.about{left:0;top:436px;width:907px;height:363px;background:var(--section-grey)}
.about h2{position:absolute;left:110px;top:64px;color:var(--green);font-size:22px;font-weight:700;letter-spacing:1px}
.rule{position:absolute;height:2px;width:32px;background:var(--green)}
.about p{position:absolute;left:110px;width:310px;font-size:7.5px;line-height:13.3px;color:var(--muted)}
.btn-small{position:absolute;left:110px;top:241px;width:59px;height:22px;background:var(--green);color:var(--white);font-size:7.5px;text-align:center;line-height:22px;border-radius:2px}

.form-card{left:462px;top:387px;width:338px;height:345px;background:var(--white)}
.form-card .head{height:50px;background:var(--green);color:var(--white);text-align:center;font-size:18px;font-weight:700;letter-spacing:1px;line-height:50px}
.field{position:absolute;width:141px}
.field label{display:block;font-size:8px;color:#222;margin-bottom:4px}
.field .input{height:29px;background:var(--field)}
.form-card .submit{position:absolute;left:23px;top:270px;width:294px;height:42px;background:var(--green);color:var(--white);font-size:12.5px;text-align:center;line-height:42px}

.story{left:0;top:799px;width:907px;height:614px}
.center-title{position:absolute;left:0;width:907px;text-align:center;font-weight:700;letter-spacing:1px;line-height:1.2}
.center-text{position:absolute;left:203px;width:501px;text-align:center;font-size:9px;line-height:14px;color:var(--muted)}
.video{left:110px;top:182px;width:691px;height:364px;background:linear-gradient(160deg,#6e6e6e 0%,#5a5b52 50%,#3f4536 100%)}
.video .play{position:absolute;left:313px;top:150px;width:64px;height:64px;border-radius:50%;border:2px solid var(--white);background:rgba(255,255,255,.15)}
.video .play svg{position:absolute;left:22px;top:18px}

.testimonial{left:0;top:1413px;width:907px;height:320px;background:var(--green);color:var(--white)}
.testimonial .quote-mark{position:absolute;left:0;width:561px;text-align:center;top:72px;font-size:64px;line-height:1;color:rgba(255,255,255,.5);font-weight:700}
.testimonial blockquote{position:absolute;left:120px;width:321px;top:135px;text-align:center;font-size:11px;line-height:14.2px}
.testimonial .who{position:absolute;left:120px;width:321px;top:221px;text-align:center;font-size:10px;font-weight:600}
.testimonial .date{position:absolute;left:120px;width:321px;top:234px;text-align:center;font-size:7.5px}
.testimonial .photo{position:absolute;left:462px;top:51px;width:338px;height:218px;background:linear-gradient(180deg,#b8a89a 0%,#8f7b69 55%,#5a4434 100%)}
.arrow{position:absolute;top:152px}

.newsletter{left:0;top:1733px;width:907px;height:262px}
.subscribe-input{position:absolute;left:270px;top:163px;width:257px;height:32px;background:var(--field);font-size:7px;color:#bbb;line-height:32px;padding-left:17px}
.subscribe-btn{position:absolute;left:527px;top:163px;width:111px;height:32px;background:var(--green);color:var(--white);font-size:9.5px;font-weight:600;text-align:center;line-height:32px}

.footer{left:0;top:1995px;width:907px;height:334px;background:var(--green);color:var(--white)}
.footer .brand-name{position:absolute;left:0;width:907px;top:128px;text-align:center;font-size:16px;font-weight:300;letter-spacing:.5px;line-height:1.2}
.footer .brand-name small{display:block;font-size:7px;letter-spacing:6px;margin-top:3px}
.footer .links{position:absolute;left:0;width:907px;text-align:center;font-size:8.5px;word-spacing:2px}
.footer .divider{position:absolute;left:241px;top:209px;width:427px;height:1px;background:rgba(255,255,255,.8)}
.footer .social{position:absolute;left:405px;top:260px;display:flex;gap:8px}
.footer .social span{width:18px;height:18px;background:var(--green-bright)}
.footer .copy{position:absolute;left:0;width:907px;top:297px;text-align:center;font-size:8px}
.band{left:0;top:2329px;width:907px;height:35px;background:var(--green-bright)}
.to-top{left:439px;top:2318px;width:22px;height:22px;background:var(--white);transform:rotate(45deg)}
.to-top-arrow{left:443px;top:2322px}
</style>
</head>
<body>
<div class="backdrop-top"></div>
<main class="page">
  <div class="abs topbar">
    <div class="abs phone">
      <svg width="11" height="11" viewBox="0 0 24 24"><path fill="#fff" d="M6.6 10.8a15.1 15.1 0 0 0 6.6 6.6l2.2-2.2c.3-.3.7-.4 1-.2 1.1.4 2.3.6 3.6.6.6 0 1 .4 1 1V20c0 .6-.4 1-1 1C10.6 21 3 13.4 3 4c0-.6.4-1 1-1h3.5c.6 0 1 .4 1 1 0 1.3.2 2.5.6 3.6.1.3 0 .7-.2 1z"/></svg>
      <span>(+1) 555-010-42</span>
    </div>
    <div class="abs social"><span></span><span></span><span></span><span></span></div>
  </div>

  <header class="abs nav">
    <div class="abs brand"><span class="dot"></span><span>Evergreen Vows<br>Weddings</span></div>
    <nav class="abs menu"><span class="active">HOME</span><span>ABOUT</span><span>SERVICES</span><span>CONTACT</span></nav>
  </header>

  <section class="abs hero" role="img" aria-label="Hillside tree nursery with terraced seedling beds among tall pines">
    <h1 class="serif">The Guide to<br>Sustainable, Zero-Waste,<br>Ethical Weddings</h1>
    <div class="more serif">More Info</div>
  </section>

  <section class="abs about">
    <h2 class="serif">WHO WE ARE</h2>
    <div class="rule" style="left:110px;top:103px"></div>
    <p style="top:117px">Lorem Ipsum is simply dummy text of the printing and typesetting industry. Lorem Ipsum has been the industry's standard dummy text ever since the 1500s, when an unknown printer took a galley of type and scrambled it to make a type specimen book. It has survived not only five centuries, but also the leap into electronic typesetting, remaining essentially unchanged.</p>
    <p style="top:196px">It has survived not only five centuries, but also the leap into electronic typesetting, remaining essentially unchanged.</p>
    <div class="btn-small">Read More</div>
  </section>

  <form class="abs form-card">
    <div class="head serif">GET AN INFORMATION</div>
    <div class="field" style="left:23px;top:81px"><label>First Name:</label><div class="input"></div></div>
    <div class="field" style="left:176px;top:81px"><label>Last Name:</label><div class="input"></div></div>
    <div class="field" style="left:23px;top:141px"><label>Email:</label><div class="input"></div></div>
    <div class="field" style="left:176px;top:141px"><label>Phone:</label><div class="input"></div></div>
    <div class="field" style="left:23px;top:201px"><label>Wedding Date:</label><div class="input"></div></div>
    <div class="field" style="left:176px;top:201px"><label>Number of guests:</label><div class="input"></div></div>
    <div class="submit">Request more information</div>
  </form>

  <section class="abs story">
    <h2 class="center-title serif" style="top:62px;font-size:22px;color:var(--green)">OUR STORY</h2>
    <div class="rule" style="left:437px;top:97px"></div>
    <p class="center-text" style="top:115px">Lorem Ipsum is simply dummy text of the printing and typesetting industry. Lorem Ipsum has been the industry's standard dummy text ever since the 1500s,</p>
    <div class="abs video" role="img" aria-label="Video still of two men talking outdoors at a tree nursery">
      <div class="play"><svg width="24" height="26" viewBox="0 0 24 26"><path fill="#fff" d="M0 0 L24 13 L0 26 Z"/></svg></div>
    </div>
  </section>

  <section class="abs testimonial">
    <svg class="arrow" style="left:76px" width="10" height="18" viewBox="0 0 10 18"><path d="M9 1 L1 9 L9 17" fill="none" stroke="#fff" stroke-width="1.3"/></svg>
    <div class="quote-mark serif">&#8220;</div>
    <blockquote class="serif">Lorem Ipsum is simply dummy text of the printing and typesetting industry. Lorem Ipsum has been the industry's standard dummy text ever since the 1500s, when an unknown printer took a galley of type and scrambled it to make a type specimen book.</blockquote>
    <div class="who">John Doe</div>
    <div class="date">03 June, 2020</div>
    <div class="photo" role="img" aria-label="Wedding couple with red bouquet behind a dessert table on a city balcony"></div>
    <svg class="arrow" style="left:827px" width="10" height="18" viewBox="0 0 10 18"><path d="M1 1 L9 9 L1 17" fill="none" stroke="#fff" stroke-width="1.3"/></svg>
  </section>

  <section class="abs newsletter">
    <h2 class="center-title serif" style="top:63px;font-size:18px;font-weight:400;color:#222">JOIN OUR NEWSLETTER</h2>
    <div class="rule" style="left:437px;top:95px;background:#222"></div>
    <p class="center-text" style="top:113px">Lorem Ipsum is simply dummy text of the printing and typesetting industry. Lorem Ipsum has been the industry's standard dummy text ever since the 1500s,</p>
    <div class="subscribe-input">Enter your Email</div>
    <div class="subscribe-btn">Subscribe</div>
  </section>

  <footer class="abs footer">
    <div class="brand-name">Evergreen Vows<small>WEDDINGS</small></div>
    <div class="links" style="top:178px">Home &nbsp;&nbsp;|&nbsp;&nbsp; About Us &nbsp;&nbsp;|&nbsp;&nbsp; Services &nbsp;&nbsp;|&nbsp;&nbsp; Contact Us</div>
    <div class="divider"></div>
    <div class="links" style="top:227px">Terms &amp; Conditions &nbsp;&nbsp;|&nbsp;&nbsp; Privacy Policy &nbsp;&nbsp;|&nbsp;&nbsp; Accessibility</div>
    <div class="social"><span></span><span></span><span></span><span></span></div>
    <div class="copy">Copyright © 2020 All Reserved.</div>
  </footer>
  <div class="abs band"></div>
  <div class="abs to-top"></div>
  <svg class="abs to-top-arrow" width="14" height="14" viewBox="0 0 14 14"><path d="M7 12 V2 M3 6 L7 2 L11 6" fill="none" stroke="#0c6e00" stroke-width="1.6"/></svg>
</main>
</body>
</html>
```